Cradlecraft by Lorna Business Card Design

i am starting a new business as a reborn artist (that is painting dolls to make them look like real live babies)

i eventually want to sell the dolls that i make and have classed in reborning. but at the moment i just want to get my name out there.

I do not currently have images of the dolls so cannot have an image in the design.

Non compulsory thoughts: i like the look of old wood, white and baby pink,even hot pink, and lace, denim. i had in mind something like a tiny baby in a old cradle or something, a old drawer, box, something different or unusual, it has to be a girl baby. i am also open to other thoughts on the matter. i would like plain writing not all swirly
Updates

Sorry to change but would like it to read country cradlecraft by lorna.

Industry/Entity Type

Painting

Contact Information for Business Card

Cradlecraft by Lorna
country babies that never grow up
Reborn Artist Lorna Whitby
0431 756 842
marlo.t@quillbox.com

```html
<!DOCTYPE html>
<html lang="en">
<head>
<meta charset="utf-8">
<title>Country Cradlecraft by Lorna – Business Card</title>
<link rel="stylesheet" href="https://fonts.googleapis.com/css2?family=Alegreya+Sans:wght@800&family=Delius&display=swap">
<style>
  :root {
    --page: #f3eee8;
    --card-band: #6f6049;
    --wood-light: #7a4a2a;
    --wood-mid: #5e3620;
    --wood-dark: #3d2214;
    --wood-edge: #2e1a10;
    --ink-cream: #efe6d4;
    --ink-white: #ffffff;
    --sketch-tone: #6a3f25;
  }
  * { margin: 0; padding: 0; box-sizing: border-box; }
  html, body {
    width: 1200px; height: 1000px; overflow: hidden;
    background: var(--page);
  }
  .stage {
    width: 1200px; height: 1000px;
    display: flex; align-items: center; justify-content: center;
  }
  .business-card {
    position: relative;
    width: 900px; height: 514px;
    background: var(--card-band);
    overflow: hidden;
    box-shadow: 0 10px 30px rgba(0,0,0,.18);
    font-family: "Delius", sans-serif;
    color: var(--ink-cream);
  }
  .wood-band { position: absolute; inset: 0; }
  .baby-sketch {
    position: absolute;
    width: 120px; height: 140px;
    border-radius: 40px;
    background: var(--sketch-tone);
  }
  .baby-sketch--left { left: 60px; top: 260px; }
  .baby-sketch--right { right: 60px; top: 120px; }
  .brand-line {
    position: absolute; left: 44px; top: 44px;
    font-size: 27px; letter-spacing: 4px; text-transform: uppercase;
  }
  .tagline {
    position: absolute; right: 44px; bottom: 42px;
    font-size: 27px; letter-spacing: 3px; text-transform: uppercase;
  }
  .contact-block {
    position: absolute; left: 0; right: 0; top: 178px;
    text-align: center; color: var(--ink-white);
  }
  .artist-name {
    font-family: "Alegreya Sans", sans-serif;
    font-weight: 800; font-size: 42px; letter-spacing: 3px;
    text-transform: uppercase;
  }
  .artist-role { font-size: 24px; margin-top: 2px; }
  .artist-phone { font-size: 24px; margin-top: 34px; letter-spacing: 1px; }
  .artist-email { font-size: 24px; margin-top: 4px; letter-spacing: 1px; }
</style>
</head>
<body>
<main class="stage">
  <section class="business-card">
    <svg class="wood-band" viewBox="0 0 900 514" width="900" height="514" role="img" aria-label="Band of old weathered wooden planks across the card">
      <defs>
        <linearGradient id="woodTone" x1="0" y1="0" x2="1" y2="1">
          <stop offset="0" stop-color="var(--wood-mid)"/>
          <stop offset="0.45" stop-color="var(--wood-light)"/>
          <stop offset="1" stop-color="var(--wood-dark)"/>
        </linearGradient>
      </defs>
      <path d="M0,118 C180,92 340,150 520,112 S790,92 900,124 L900,398 C720,424 560,368 400,398 S150,426 0,392 Z"
            fill="url(#woodTone)" stroke="var(--wood-edge)" stroke-width="10"/>
    </svg>
    <div class="baby-sketch baby-sketch--left" role="img" aria-label="White line drawing of a baby"></div>
    <div class="baby-sketch baby-sketch--right" role="img" aria-label="White line drawing of a baby"></div>

    <p class="brand-line">Country Cradlecraft by Lorna</p>

    <div class="contact-block">
      <h1 class="artist-name">Lorna Whitby</h1>
      <p class="artist-role">Reborn Artist</p>
      <p class="artist-phone">0431 756 842</p>
      <p class="artist-email">marlo.t@quillbox.com</p>
    </div>

    <p class="tagline">Babies that never grow up</p>
  </section>
</main>
</body>
</html>
```